Design the Keystone HR business card for my new business

I've just had a logo designed (attached) for my new business doing HR consulting. I'm a one person operation at this stage, my aim is to provide support and help to small to medium sized businesses with their people objectives or issues.

I'm not really into anything overly flashy, I'm not a PR or marketing agency. I'd like my card to look modern, professional and not gimmicky.

I'm thinking black front (to go with logo), double sided with details on the back, maybe in a different colour?

Logo attached in several different formats.

Front of the card to have logo and added text: People and Development Solutions

Back of the card to also feature logo in some way and say:
Megan Tulloch
PO Box (TBA)
Marrowvale QLD 4391
0438 512 976
megan@keystonehr.com.au
www.keystonehr.com.au

Target Market(s)

Small to medium businesses / business owners.

Industry/Entity Type

Marketing

Requirements
Must have
• Double sided business card.
Should not have
• Anything overly gimmicky.

```html
<!DOCTYPE html>
<html lang="en">
<head>
<meta charset="utf-8">
<title>Keystone HR — Business Card</title>
<link rel="stylesheet" href="https://fonts.googleapis.com/css2?family=Questrial&display=swap">
<style>
  :root {
    --page: #ffffff;
    --card-black: #0b0b0c;
    --violet-deep: #3d10d6;
    --violet-mid: #6a2ee8;
    --violet-soft: #a65af4;
    --violet-glow: rgba(120, 60, 240, 0.55);
    --text-light: #ffffff;
    --text-muted: #e9e2ff;
  }
  * { margin: 0; padding: 0; box-sizing: border-box; }
  html, body {
    width: 1200px;
    height: 495px;
    overflow: hidden;
    background: var(--page);
    font-family: "Questrial", "Century Gothic", sans-serif;
  }
  .canvas { position: relative; width: 1200px; height: 495px; }

  .card {
    position: absolute;
    width: 476px;
    height: 265px;
    overflow: hidden;
    color: var(--text-light);
  }
  .card--front { left: 102px; top: 115px; background: var(--card-black); }
  .card--back {
    left: 622px; top: 113px;
    background: linear-gradient(115deg, var(--violet-deep) 0%, var(--violet-mid) 50%, var(--violet-soft) 100%);
  }

  .card__decoration {
    position: absolute;
    top: 0; right: 0;
    width: 220px; height: 100%;
  }
  .card--front .card__decoration {
    background: radial-gradient(ellipse at 0% 100%, transparent 55%, var(--violet-glow) 75%, rgba(90, 40, 200, 0.15) 100%);
  }
  .card--back .card__decoration {
    background: radial-gradient(ellipse at 0% 100%, transparent 55%, rgba(255, 255, 255, 0.12) 78%, rgba(255, 255, 255, 0.04) 100%);
  }

  .brand {
    position: absolute;
    display: flex;
    align-items: center;
    gap: 28px;
  }
  .card--front .brand { left: 38px; top: 42px; }
  .card--back .brand { left: 40px; top: 42px; }
  .brand__mark {
    width: 58px; height: 58px;
    border-radius: 50%;
    border: 1.5px solid var(--violet-soft);
    flex: none;
  }
  .card--back .brand__mark { border-color: var(--text-light); }
  .brand__name {
    font-size: 33px;
    line-height: 1;
    letter-spacing: -0.5px;
    color: var(--text-light);
    font-weight: 400;
  }

  .tagline {
    position: absolute;
    left: 126px;
    top: 213px;
    font-size: 13px;
    color: var(--text-light);
  }

  .contact {
    position: absolute;
    left: 128px;
    top: 111px;
    font-size: 13px;
    line-height: 15.5px;
    font-style: normal;
  }
  .contact__name { margin-bottom: 16px; }
  .contact__address { margin-bottom: 16px; }
</style>
</head>
<body>
  <main class="canvas">
    <section class="card card--front" aria-label="Business card front">
      <div class="card__decoration" role="img" aria-label="Sweeping violet arc lines fanning across the right edge"></div>
      <div class="brand">
        <span class="brand__mark"></span>
        <span class="brand__name">Keystone HR</span>
      </div>
      <p class="tagline">People and Development Solutions</p>
    </section>

    <section class="card card--back" aria-label="Business card back">
      <div class="card__decoration" role="img" aria-label="Faint light arc lines fanning across the right edge"></div>
      <div class="brand">
        <span class="brand__mark"></span>
        <span class="brand__name">Keystone HR</span>
      </div>
      <address class="contact">
        <p class="contact__name">Megan Tulloch</p>
        <p class="contact__address">PO Box (TBA)<br>Marrowvale QLD 4391<br>0438 512 976</p>
        <p class="contact__web">megan@keystonehr.com.au<br>www.keystonehr.com.au</p>
      </address>
    </section>
  </main>
</body>
</html>
```